Corvanta Business cards template

We're looking for something modern and elegant. We are a reseller of technology (computers, datacenter, etc). Color theme would be "only" white with the incorporation of the blue that's present on our website (Corvanta.com) and logo file. We would like for the card to provide all the necessary info for the specific person (Phone#, fax#, email, name, website URL) . I'm attaching the logo file to this request. Please have it show Montreal/New York somewhere, without providing specific addresses.

Target Market(s)

All b2b

Industry/Entity Type

Business

Contact Information for Business Card

Please have the color scheme be represented by only the white and blue from our website (Corvanta.com) and logo. We would like to logo on the card, but not big and overwhelming. This card will be used as a template for anybody within the company, it should display the user's name, phone#, fax#, email, job title and website URL. Please have it show Montreal/New York somewhere, without providing our specific addresses. Really, we're looking for a clean, simple and elegant look.

Font styles to use
Serif

Requirements
Must have
• Please see card details
Nice to have
• Please see card details
Should not have
• Anything tacky or tagline.

```html
<!DOCTYPE html>
<html lang="en">
<head>
<meta charset="utf-8">
<title>Corvanta Business Card</title>
<link rel="stylesheet" href="https://fonts.googleapis.com/css2?family=Tinos&display=swap">
<style>
  :root {
    --page: #e4e4e4;
    --paper: #ffffff;
    --blue-light: #66b8ec;
    --blue-mid: #2a8bd0;
    --blue-deep: #0a70bb;
    --blue-dark: #0b5b93;
    --brand: #0a7cc4;
    --ink: #0b5b93;
    --on-dark: #ffffff;
  }
  html, body {
    margin: 0;
    padding: 0;
    width: 1200px;
    height: 990px;
    overflow: hidden;
    background: var(--page);
    font-family: "Tinos", "Times New Roman", serif;
  }
  .canvas { position: relative; width: 1200px; height: 990px; }
  .card {
    position: absolute;
    background: var(--paper);
    overflow: hidden;
    box-shadow: 2px 3px 6px rgba(0,0,0,0.35);
  }
  .card--front { left: 278px; top: 126px; width: 631px; height: 378px; }
  .card--back  { left: 278px; top: 533px; width: 628px; height: 376px; }
  .card__waves { position: absolute; inset: 0; width: 100%; height: 100%; }
  .wave { filter: drop-shadow(-2px 0 3px rgba(0,0,0,0.3)); }
  .brand-name {
    position: absolute;
    margin: 0;
    color: var(--brand);
    font-weight: 400;
    line-height: 1;
    white-space: nowrap;
  }
  .card--front .brand-name { left: 92px; top: 166px; font-size: 80px; letter-spacing: 2px; }
  .card--back .brand-name  { left: 46px; top: 174px; font-size: 62px; letter-spacing: 1px; }
  .person {
    position: absolute;
    left: 54px;
    width: 200px;
    text-align: center;
    color: var(--ink);
    font-size: 21px;
    margin: 0;
    line-height: 1;
  }
  .person--name { top: 274px; }
  .person--job  { top: 307px; }
  .contact {
    position: absolute;
    color: var(--on-dark);
    white-space: nowrap;
    display: flex;
    align-items: center;
    line-height: 1;
  }
  .contact svg { flex: none; }
  .contact--phone { left: 354px; top: 70px;  font-size: 27px; gap: 16px; }
  .contact--fax   { left: 344px; top: 116px; font-size: 22px; gap: 12px; }
  .contact--email { left: 336px; top: 160px; font-size: 21px; gap: 8px; }
  .contact--web   { left: 328px; top: 208px; font-size: 21px; gap: 10px; transform: scaleX(0.86); transform-origin: left center; }
  .contact--place { left: 318px; top: 260px; font-size: 21px; gap: 14px; }
</style>
</head>
<body>
<main class="canvas">

  <section class="card card--front" aria-label="Card front">
    <svg class="card__waves" viewBox="0 0 631 378" aria-hidden="true">
      <path class="wave" d="M0 0 L70 0 Q74 160 0 258 Z" fill="var(--blue-mid)"/>
      <path class="wave" d="M0 0 L64 0 Q64 130 0 210 Z" fill="var(--blue-deep)"/>
      <path class="wave" d="M0 0 L58 0 Q54 80 0 120 Z" fill="var(--blue-dark)"/>
      <path class="wave" d="M454 378 Q490 170 631 86 L631 378 Z" fill="var(--blue-light)"/>
      <path class="wave" d="M458 378 Q510 220 631 136 L631 378 Z" fill="var(--blue-mid)"/>
      <path class="wave" d="M462 378 Q530 260 631 190 L631 378 Z" fill="var(--blue-deep)"/>
      <path class="wave" d="M466 378 Q550 290 631 240 L631 378 Z" fill="var(--blue-dark)"/>
    </svg>
    <h1 class="brand-name">Corvanta</h1>
  </section>

  <section class="card card--back" aria-label="Card back">
    <svg class="card__waves" viewBox="0 0 628 376" aria-hidden="true">
      <path class="wave" d="M426 0 Q325 140 322 376 L628 376 L628 0 Z" fill="var(--blue-light)"/>
      <path class="wave" d="M540 0 Q360 100 326 376 L628 376 L628 0 Z" fill="var(--blue-mid)"/>
      <path class="wave" d="M628 28 Q400 110 330 376 L628 376 Z" fill="var(--blue-deep)"/>
      <path class="wave" d="M628 70 Q420 150 336 376 L628 376 Z" fill="var(--blue-dark)"/>
    </svg>

    <h2 class="brand-name">Corvanta</h2>
    <p class="person person--name">Name</p>
    <p class="person person--job">Job</p>

    <div class="contact contact--phone">
      <svg width="40" height="30" viewBox="0 0 40 30" aria-hidden="true">
        <path d="M2 8 Q20 -2 38 8 L36 13 L29 11 L29 7 Q20 4 11 7 L11 11 L4 13 Z" fill="#fff"/>
        <path d="M9 14 L31 14 L35 29 L5 29 Z" fill="#fff"/>
        <circle cx="20" cy="21" r="4.5" fill="var(--blue-dark)"/>
      </svg>
      <span>+15145550142</span>
    </div>

    <div class="contact contact--fax">
      <svg width="36" height="32" viewBox="0 0 36 32" aria-hidden="true">
        <rect x="9" y="2" width="18" height="10" fill="none" stroke="#fff" stroke-width="2"/>
        <rect x="2" y="11" width="32" height="14" rx="2" fill="#fff"/>
        <rect x="9" y="20" width="18" height="10" fill="#fff" stroke="var(--blue-dark)" stroke-width="1.6"/>
        <circle cx="28" cy="15" r="1.8" fill="var(--blue-dark)"/>
      </svg>
      <span>Fax +15145550143</span>
    </div>

    <div class="contact contact--email">
      <svg width="38" height="38" viewBox="0 0 38 38" aria-hidden="true">
        <circle cx="19" cy="19" r="17" fill="none" stroke="#fff" stroke-width="2"/>
        <rect x="9" y="12" width="20" height="14" fill="#fff"/>
        <path d="M9 12 L19 20 L29 12" fill="none" stroke="var(--blue-mid)" stroke-width="1.6"/>
      </svg>
      <span>hello@corvanta-mail.com</span>
    </div>

    <div class="contact contact--web">
      <svg width="40" height="40" viewBox="0 0 40 40" aria-hidden="true">
        <g fill="none" stroke="#fff" stroke-width="2">
          <circle cx="17" cy="17" r="14"/>
          <ellipse cx="17" cy="17" rx="6" ry="14"/>
          <path d="M3 17 H31 M6 9 H28 M6 25 H28"/>
        </g>
        <path d="M24 22 L36 30 L31 31 L34 37 L31 38 L28 32 L24 35 Z" fill="#fff"/>
      </svg>
      <span>WWW.CORVANTA.COM</span>
    </div>

    <div class="contact contact--place">
      <svg width="34" height="40" viewBox="0 0 34 40" aria-hidden="true">
        <ellipse cx="17" cy="33" rx="15" ry="5" fill="none" stroke="#fff" stroke-width="2"/>
        <path d="M17 32 Q6 18 6 12 A11 11 0 0 1 28 12 Q28 18 17 32 Z" fill="#fff"/>
        <circle cx="17" cy="12" r="4" fill="var(--blue-mid)"/>
      </svg>
      <span>Montreal / New York</span>
    </div>
  </section>

</main>
</body>
</html>
```